RV park billboard

We need a billboard for cedar bend RV park . I was thinking about having a big orange in the background. We will have free fiber optic internet and each camper will have its own personal hotspot and we want that on the sign... Also the phone number with the area code... But I don't have the exact number yet. Size of sign will be 12 x 40
Updates
Make sure sign has Cedar Bend RV park on it
Target Market(s)
Plant turnaround workers
Look and feel

```html
<!DOCTYPE html>
<html lang="en">
<head>
<meta charset="utf-8">
<title>Cedar Bend RV park billboard</title>
<link rel="stylesheet" href="https://fonts.googleapis.com/css2?family=Fira+Sans:wght@400;700;800&family=Source+Sans+3:wght@800&family=Montserrat:wght@800&display=swap">
<style>
  :root {
    --page: #eef2f5;
    --white: #ffffff;
    --green: #7dc242;
    --orange-top: #fbb21f;
    --orange-bottom: #f47b20;
    --orange-deep: #e0742a;
    --orange-mid: #f68a1f;
  }
  * { margin: 0; padding: 0; box-sizing: border-box; }
  html, body {
    width: 1200px;
    height: 815px;
    overflow: hidden;
    background: var(--page);
  }
  .billboard {
    position: absolute;
    left: 20px;
    top: 233px;
    width: 1160px;
    height: 348px;
    background: linear-gradient(180deg, var(--orange-top) 0%, var(--orange-bottom) 100%);
    overflow: hidden;
  }
  .title-band {
    position: absolute;
    left: 0; top: 0;
    width: 100%;
    height: 99px;
    background: var(--white);
  }
  .park-name {
    position: absolute;
    right: 14px;
    top: 2px;
    font-family: "Source Sans 3", sans-serif;
    font-weight: 800;
    font-size: 84px;
    line-height: 96px;
    color: var(--green);
    white-space: nowrap;
  }
  .fruit-art {
    position: absolute;
    left: 26px;
    top: 17px;
    width: 414px;
    height: 308px;
    border-radius: 50%;
    background: radial-gradient(ellipse at 40% 55%, var(--orange-mid) 0%, var(--orange-deep) 70%, var(--orange-bottom) 100%);
  }
  .feature {
    position: absolute;
    top: 126px;
    color: var(--white);
    font-family: "Fira Sans", sans-serif;
  }
  .feature--hotspot { left: 488px; }
  .feature--fiber { left: 812px; }
  .feature-icon {
    position: absolute;
    left: 0;
    top: 2px;
  }
  .feature-text {
    margin-left: 69px;
  }
  .feature--fiber .feature-text { margin-left: 57px; }
  .feature-heading {
    font-weight: 800;
    font-size: 42px;
    line-height: 55px;
  }
  .feature-note {
    font-weight: 400;
    font-size: 22px;
    line-height: 24px;
    letter-spacing: 0.04em;
    margin-top: -4px;
  }
  .phone-band {
    position: absolute;
    left: 488px;
    top: 279px;
    width: 672px;
    height: 57px;
    background: var(--white);
  }
  .phone-number {
    position: absolute;
    left: 60px;
    top: 0;
    font-family: "Montserrat", sans-serif;
    font-weight: 800;
    font-size: 44px;
    line-height: 57px;
    letter-spacing: 0.3em;
    color: var(--orange-bottom);
    white-space: nowrap;
  }
</style>
</head>
<body>
  <section class="billboard">
    <div class="title-band"></div>
    <h1 class="park-name">Cedar Bend RV park</h1>

    <div class="fruit-art" role="img" aria-label="Illustration of two large oranges with green leaves"></div>

    <div class="feature feature--hotspot">
      <svg class="feature-icon" width="58" height="46" viewBox="0 0 58 46" aria-hidden="true">
        <g fill="none" stroke="#ffffff" stroke-width="5" stroke-linecap="round">
          <path d="M4 16 A36 36 0 0 1 54 16"/>
          <path d="M12 25 A24 24 0 0 1 46 25"/>
          <path d="M20 34 A12 12 0 0 1 38 34"/>
        </g>
        <circle cx="29" cy="41" r="4" fill="#ffffff"/>
      </svg>
      <div class="feature-text">
        <p class="feature-heading">Personal<br>hotspot</p>
        <p class="feature-note">for each camper</p>
      </div>
    </div>

    <div class="feature feature--fiber">
      <svg class="feature-icon" width="40" height="50" viewBox="0 0 40 50" aria-hidden="true">
        <g fill="none" stroke="#ffffff" stroke-width="2.5" stroke-linecap="round">
          <path d="M20 30 L20 6"/>
          <path d="M20 30 Q14 18 6 12"/>
          <path d="M20 30 Q26 18 34 12"/>
        </g>
        <g fill="#ffffff">
          <circle cx="20" cy="5" r="3"/>
          <circle cx="5" cy="11" r="3"/>
          <circle cx="35" cy="11" r="3"/>
          <rect x="13" y="30" width="14" height="18" rx="2"/>
        </g>
      </svg>
      <div class="feature-text">
        <p class="feature-heading">Free<br>fiber optic</p>
        <p class="feature-note">internet</p>
      </div>
    </div>

    <div class="phone-band">
      <p class="phone-number">(409) 555-0142</p>
    </div>
  </section>
</body>
</html>
```